'WILD' eye catching Business Card Design / Logo for production company / TV host / adventurer

Hi there,

We are looking for a 'WILD' and exciting logo and double sided business card for our business "Red Kettle Studios".

Corwin Baxley is an international television host, adventurer, author and inspirational public speaker.

We want to project Corwin's talents onto his business card.

We are looking for a business card design that can carry over onto letter heads, emails etc. We want a design that is 'WILD', different and exciting.

Feel free to check out Corwin's web site: www.redkettlestudios.co.nz to get a better understanding what he is about.

Please feel free to go completely 'WILD' on this project as we want something different with lots of WOW factors.

Thank you so much and we look forward to your designs.

We have a feeling that there will be many more designs in the near future.

Best regards,

the production team

We have added another task to the list.

If the winning designer can also provide us with a matching letterhead and email signature based on the same style of design as the business card.

Target Market(s)

People with passion.

Industry/Entity Type

Business

Requirements
Must have
• Red Kettle Studios
Corwin Baxley
42 Fernhill Lane
Ashbury 7388
New Zealand

Phone +64-(0)3-5027 416
Cell +64-(0)274-861 052

email: redkettlenz@mailbox-example.nz
www.redkettlestuios.co.nz
Nice to have
• A feature made out of the name 'Red Kettle Studios'.

Corwin Baxley's name reasonably obvious.

All other details (except web site) can be quite small.

```html
<!DOCTYPE html>
<html lang="en">
<head>
<meta charset="utf-8">
<title>Red Kettle Studios – Business Card</title>
<link href="https://fonts.googleapis.com/css2?family=Gochi+Hand&family=Open+Sans:wght@700&display=swap" rel="stylesheet">
<style>
  :root {
    --stage: #cdcdcd;
    --card-white: #ffffff;
    --paper-light: #f1eed6;
    --paper-mid: #e6e2bf;
    --paper-deep: #d9d3a6;
    --ink-dark: #38372f;
    --ink-red: #8e1c10;
    --shadow: rgba(0, 0, 0, 0.45);
  }
  html, body {
    margin: 0;
    padding: 0;
    width: 1200px;
    height: 988px;
    overflow: hidden;
    background: var(--stage);
  }
  .canvas {
    position: relative;
    width: 1200px;
    height: 988px;
  }
  .card {
    position: absolute;
    left: 354px;
    width: 490px;
    height: 273px;
    border-radius: 18px;
    overflow: hidden;
    background: var(--card-white);
    box-shadow: 3px 5px 9px var(--shadow);
  }
  .card--front { top: 177px; }
  .card--back { top: 537px; }
  .paper-texture {
    position: absolute;
    left: 0;
    top: 0;
    width: 100%;
    background:
      radial-gradient(ellipse at 20% 30%, var(--paper-light) 0%, transparent 60%),
      radial-gradient(ellipse at 85% 80%, var(--paper-deep) 0%, transparent 55%),
      linear-gradient(160deg, var(--paper-light) 0%, var(--paper-mid) 55%, var(--paper-deep) 100%);
  }
  .card--front .paper-texture { height: 100%; }
  .card--back .paper-texture { height: 122px; }
  .brand-name {
    position: absolute;
    margin: 0;
    font-family: "Gochi Hand", cursive;
    font-weight: 400;
    color: var(--ink-dark);
    white-space: nowrap;
    line-height: 1;
  }
  .card--front .brand-name {
    right: 38px;
    top: 96px;
    font-size: 48px;
  }
  .card--back .brand-name {
    left: 0;
    right: 0;
    text-align: center;
    top: 45px;
    font-size: 38px;
  }
  .person-name {
    position: absolute;
    margin: 0;
    font-family: "Gochi Hand", cursive;
    color: var(--ink-red);
    white-space: nowrap;
    line-height: 1;
  }
  .card--front .person-name {
    right: 41px;
    top: 160px;
    font-size: 26px;
  }
  .card--back .person-name {
    left: 266px;
    top: 147px;
    font-size: 25px;
  }
  .contact {
    position: absolute;
    right: 256px;
    top: 141px;
    margin: 0;
    font-family: "Open Sans", Arial, sans-serif;
    font-weight: 700;
    font-size: 12px;
    line-height: 15.5px;
    color: var(--ink-dark);
    text-align: right;
    font-style: normal;
    white-space: nowrap;
  }
  .contact p { margin: 0; }
  .contact .gap { margin-top: 14px; }
  .contact .web { color: var(--ink-red); }
</style>
</head>
<body>
<div class="canvas">

  <section class="card card--front">
    <div class="paper-texture" role="img" aria-label="Weathered parchment paper texture in pale cream and olive tones"></div>
    <h1 class="brand-name">Red Kettle Studios</h1>
    <p class="person-name">Corwin Baxley</p>
  </section>

  <section class="card card--back">
    <div class="paper-texture" role="img" aria-label="Weathered parchment paper texture band in pale cream and olive tones"></div>
    <h2 class="brand-name">Red Kettle Studios</h2>
    <address class="contact">
      <p>42 Fernhill Lane</p>
      <p>Ashbury 7388, New Zealand</p>
      <p class="gap">Phone: +64 (0) 3-5027 416</p>
      <p>Cell: +64 (0) 274-861 052</p>
      <p>redkettlenz@mailbox-example.nz</p>
      <p class="web">www.redkettlestuios.co.nz</p>
    </address>
    <p class="person-name">Corwin Baxley</p>
  </section>

</div>
</body>
</html>
```